Q7M Electrical Systems Inc Business Cards

Target Market(s)

Customers

Industry/Entity Type

Construction - Electrical

Contact Information for Business Card

Company Name, Address, Phone, and email address

Font styles to use
Sans Serif

Colors
0054AA
0677BA
7BADD7
CADEEF
E8F1F8

Requirements
Must have
• we would like to use the same design that we had our vehicles wrapped
Nice to have
• The design that we used on our trucks

```html
<!DOCTYPE html>
<html lang="en">
<head>
<meta charset="utf-8">
<title>Q7M Electrical Systems Inc – Business Cards</title>
<link rel="stylesheet" href="https://fonts.googleapis.com/css2?family=Poppins:wght@400;600&display=swap">
<style>
  :root {
    --stage: #3a3a3c;
    --navy: #0a1448;
    --navy-deep: #071038;
    --royal: #1b3a9e;
    --white: #ffffff;
    --rim: #c9cdd9;
    --ink: #141d4f;
  }
  * { margin: 0; padding: 0; box-sizing: border-box; }
  html, body { width: 1200px; height: 689px; overflow: hidden; }
  body {
    background: var(--stage);
    font-family: "Poppins", sans-serif;
    position: relative;
  }
  .card {
    position: absolute;
    top: 190px;
    width: 540px;
    height: 309px;
    border-radius: 22px;
    overflow: hidden;
    box-shadow: 0 14px 30px rgba(0,0,0,.45);
  }
  /* Back of card */
  .card--back {
    left: 40px;
    background: linear-gradient(135deg, var(--royal) 0%, var(--navy) 55%, var(--navy-deep) 100%);
    color: var(--white);
    display: flex;
    flex-direction: column;
    align-items: center;
    justify-content: center;
    text-align: center;
  }
  .card--back .brand-name {
    font-size: 30px;
    font-weight: 600;
    color: #1f3aa8;
    line-height: 1.1;
    margin-bottom: 4px;
  }
  .card--back .brand-rule {
    width: 250px;
    height: 1px;
    background: #1f3aa8;
    margin-bottom: 22px;
  }
  .review-line { font-size: 17px; line-height: 1.5; }
  .follow-line {
    font-size: 17px;
    line-height: 1.5;
    display: flex;
    align-items: center;
    gap: 8px;
  }
  .social-dot {
    width: 16px; height: 16px;
    border: 1.5px solid var(--white);
    border-radius: 50%;
  }
  /* Front of card */
  .card--front {
    left: 620px;
    background: var(--navy);
    color: var(--white);
  }
  .front-arc {
    position: absolute;
    inset: 0;
  }
  .front-brand {
    position: absolute;
    top: 62px;
    right: 34px;
    width: 260px;
    text-align: center;
    color: var(--ink);
  }
  .front-brand .brand-name {
    font-size: 28px;
    font-weight: 600;
    line-height: 1.15;
  }
  .front-brand .brand-rule {
    height: 1.5px;
    background: var(--ink);
    margin: 8px 10px 0;
  }
  .contact-list {
    position: absolute;
    left: 34px;
    bottom: 34px;
    list-style: none;
    font-size: 15px;
    line-height: 1.7;
  }
  .contact-item { display: flex; align-items: center; gap: 8px; }
  .contact-icon {
    width: 18px; height: 18px;
    border-radius: 50%;
    background: var(--white);
    display: flex; align-items: center; justify-content: center;
  }
  .contact-address { margin-top: 12px; line-height: 1.4; }
</style>
</head>
<body>

  <section class="card card--back" aria-label="Card back">
    <div class="brand-name">Q7M Electrical<br>Systems Inc</div>
    <div class="brand-rule"></div>
    <p class="review-line">Got a minute? Review us! Thanks.</p>
    <p class="follow-line">Follow us on <span class="social-dot"></span></p>
  </section>

  <section class="card card--front" aria-label="Card front">
    <svg class="front-arc" width="540" height="309" viewBox="0 0 540 309">
      <circle cx="430" cy="20" r="232" fill="var(--rim)"/>
      <circle cx="440" cy="10" r="222" fill="var(--white)"/>
    </svg>

    <div class="front-brand">
      <div class="brand-name">Q7M Electrical<br>Systems Inc</div>
      <div class="brand-rule"></div>
    </div>

    <ul class="contact-list">
      <li class="contact-item">
        <span class="contact-icon">
          <svg width="11" height="11" viewBox="0 0 24 24"><path fill="#0a1448" d="M6.6 10.8a15.1 15.1 0 0 0 6.6 6.6l2.2-2.2c.3-.3.7-.4 1-.2 1.1.4 2.3.6 3.6.6.6 0 1 .4 1 1V20c0 .6-.4 1-1 1A17 17 0 0 1 3 4c0-.6.4-1 1-1h3.5c.6 0 1 .4 1 1 0 1.3.2 2.5.6 3.6.1.3 0 .7-.2 1z"/></svg>
        </span>
        407-555-0148
      </li>
      <li class="contact-item">
        <span class="contact-icon">
          <svg width="11" height="11" viewBox="0 0 24 24"><rect x="2" y="5" width="20" height="14" rx="2" fill="#0a1448"/><path d="M3 6l9 7 9-7" stroke="#fff" stroke-width="1.8" fill="none"/></svg>
        </span>
        info@q7melectric.com
      </li>
      <li class="contact-address">412 Harbor Pine Way # 210,<br>Lakemont Springs, FL 32799</li>
    </ul>
  </section>

</body>
</html>
```